International Company needs a Letterhead & Envelope Design

Our Company name is Brightfold Harbor Limited.
We'd like to ask the Designers for the luxurious and sophisticated design. Our logo is very simple and neat with letter logos, so we look forward to more professional and refined designs from Designers.
We look forward to providing you with a great design.
Thanks very much in advance.

```html
<!DOCTYPE html>
<html lang="en">
<head>
<meta charset="utf-8">
<title>Brightfold Harbor Limited – Stationery</title>
<link href="https://fonts.googleapis.com/css2?family=Source+Sans+3:wght@400;600&display=swap" rel="stylesheet">
<style>
  :root{
    --maroon:#241216;
    --maroon-soft:#33202a;
    --gold:#6d6223;
    --mark-grey:#7d7b7c;
    --ink:#1c1c1c;
    --paper:#ffffff;
    --pattern:#f3f1ec;
    --light-text:#ffffff;
  }
  *{margin:0;padding:0;box-sizing:border-box}
  html,body{width:768px;height:1200px;overflow:hidden;background:#fff}
  body{position:relative;font-family:"Source Sans 3",Arial,sans-serif;color:var(--ink)}
  .sheet{position:absolute;overflow:hidden}
  .abs{position:absolute}

  /* Letterhead */
  .letterhead{left:146px;top:42px;width:475px;height:675px;background:var(--paper);border-left:1px solid #ddd;border-right:1px solid #ddd}
  .letterhead .pattern{left:0;top:60px;width:475px;height:600px;background:radial-gradient(circle at 50% 55%,var(--pattern) 0,#f8f7f3 45%,var(--paper) 70%)}
  .brand-word{font-family:"Source Sans 3",sans-serif;font-weight:600;color:var(--mark-grey);letter-spacing:2px;white-space:nowrap}
  .letterhead .brand-word{left:0;width:475px;top:22px;text-align:center;font-size:22px}
  .date{left:360px;top:64px;font-size:11px}
  .sender{left:46px;top:132px;font-size:10px;line-height:13.5px}
  .phones{left:48px;top:225px;font-size:10px;line-height:13.5px}
  .greeting{left:164px;top:130px;font-size:11px;line-height:15.5px}
  .body-copy{left:168px;top:196px;width:282px;font-size:10.4px;line-height:14px;text-align:justify}
  .body-copy p{margin-bottom:14px}
  .signature{left:168px;top:468px;width:82px;height:34px;background:linear-gradient(90deg,#e8e6e3,#f3f2f0);border-radius:3px}
  .signer{left:167px;top:503px;font-size:10.4px;line-height:12.5px}
  .footer-contact{font-size:7.5px;color:var(--light-text);display:flex;align-items:center;gap:3px}
  .footer-contact svg{flex:none}

  /* Envelope front */
  .envelope-front{left:146px;top:730px;width:475px;height:212px;background:var(--maroon)}
  .envelope-front .gold-rule{left:0;top:21px;width:475px;height:3px;background:var(--gold)}
  .envelope-front .brand-word{left:24px;top:40px;font-size:30px}
  .envelope-front .pattern{left:-40px;top:90px;width:160px;height:160px;border-radius:50%;background:radial-gradient(circle,#2e1c21 0,#2b191e 60%,var(--maroon) 72%)}
  .recipient{left:322px;top:73px;font-family:Arial,Helvetica,sans-serif;font-size:11px;line-height:13.2px;color:var(--light-text)}

  /* Envelope back */
  .envelope-back{left:146px;top:958px;width:475px;height:212px;background:var(--maroon)}
  .envelope-back .pattern{left:372px;top:110px;width:170px;height:170px;border-radius:50%;background:radial-gradient(circle,#2e1c21 0,#2b191e 60%,var(--maroon) 72%)}
  .mark-frame{left:193px;top:141px;width:90px;height:35px;border:1.5px solid var(--mark-grey);display:flex;align-items:center;justify-content:center}
  .mark-frame .brand-word{position:static;font-size:11px;letter-spacing:1px}
  .envelope-back .gold-rule{left:0;top:190px;width:475px;height:3px;background:var(--gold)}
</style>
</head>
<body>

<section class="sheet letterhead">
  <div class="abs pattern" role="img" aria-label="Faint circular key-pattern ornament in the page background"></div>
  <svg class="abs" style="left:0;top:0" width="475" height="110" viewBox="0 0 475 110">
    <rect x="0" y="0" width="475" height="14" fill="var(--maroon)"/>
    <polygon points="84,14 238,100 392,14" fill="var(--maroon)"/>
    <polyline points="0,15 84,15 238,101 392,15 475,15" fill="none" stroke="var(--gold)" stroke-width="3"/>
  </svg>
  <div class="abs brand-word">BRIGHTFOLD</div>
  <div class="abs date">Date: 26.02.2019</div>

  <div class="abs sender">Brightfold Harbor Ltd.<br>Premiun Resources<br>for Coustomer</div>
  <div class="abs phones">0044 (0) 20 55 0182<br>F: +0423000918</div>

  <div class="abs greeting">Dear<br>Lorem ipsum dolor<br>consectetuer adipiscing elit</div>

  <div class="abs body-copy">
    <p>Lorem ipsum dolor sit amet, consectetuer adipiscing elit, sed diam nonummy nibh euismod .</p>
    <p>tincidunt ut laoreet dolore magna aliquam erat volutpat. Ut wisi enim adminim veniam, quis nostrud exerci tation ullamcorper suscipit lobortis nisl ut aliquip ex ea commodo consequat. Duis autem vel eum iriure dolor in hendrerit in vulputate velit esse molestie consequat.</p>
    <p>vel illum dolore eu feugiat nulla facilisis at vero eros et accumsan et iusto odio dignissim qui blandit praesent luptatum zzril delenit augue duis dolore te feugait nulla facilisi.</p>
    <p>Lorem ipsum dolor sit amet, cons ectetuer adipiscing elit, sed diam nonummy nibh euismod tincidunt ut laoreet dolore magna aliquam erat volutpat.</p>
    <p>Ut wisi enim ad minim veniam, quis</p>
  </div>

  <div class="abs signature" role="img" aria-label="Handwritten signature of Marisol Everhart"></div>
  <div class="abs signer">Marisol Everhart<br>Chairman</div>

  <svg class="abs" style="left:0;top:590px" width="475" height="85" viewBox="0 0 475 85">
    <polygon points="0,8 238,46 475,8 475,85 0,85" fill="var(--maroon)"/>
    <polyline points="0,8 238,46 475,8" fill="none" stroke="var(--gold)" stroke-width="3"/>
    <rect x="0" y="80" width="475" height="3" fill="var(--gold)"/>
  </svg>
  <div class="abs footer-contact" style="left:47px;top:629px">
    <svg width="9" height="9" viewBox="0 0 10 10"><circle cx="5" cy="5" r="4.2" fill="none" stroke="#fff" stroke-width="1"/><path d="M1 5h8M5 1c-2 2.5-2 5.5 0 8M5 1c2 2.5 2 5.5 0 8" fill="none" stroke="#fff" stroke-width=".7"/></svg>
    www.brightfoldharbor.com
  </div>
  <div class="abs footer-contact" style="left:47px;top:641px">
    <svg width="9" height="9" viewBox="0 0 10 10"><rect x="1" y="2" width="8" height="6" fill="none" stroke="#fff" stroke-width="1"/><path d="M1 2l4 3 4-3" fill="none" stroke="#fff" stroke-width=".8"/></svg>
    hello@brightfoldharbor.com
  </div>
  <div class="abs footer-contact" style="left:301px;top:636px">
    <svg width="12" height="12" viewBox="0 0 12 12"><circle cx="6" cy="6" r="5.3" fill="none" stroke="#fff" stroke-width="1"/><path d="M6 9.5C4 7 3.8 5.9 3.8 5a2.2 2.2 0 014.4 0c0 .9-.2 2-2.2 4.5z" fill="#fff"/></svg>
    82 Lantern Quay Road, Chicago, IL
  </div>
</section>

<section class="sheet envelope-front">
  <div class="abs gold-rule"></div>
  <div class="abs pattern" role="img" aria-label="Faint circular key-pattern ornament in the lower left corner"></div>
  <div class="abs brand-word">BRIGHTFOLD</div>
  <div class="abs recipient">MR. Tobin Ashcroft<br>Director<br>Weaver Design School<br>4/F Calder Row<br>London</div>
</section>

<section class="sheet envelope-back">
  <svg class="abs" style="left:0;top:0" width="475" height="70" viewBox="0 0 475 70" role="img" aria-label="Envelope flap with a band of key-pattern borders">
    <path d="M0 0H475V50Q473 66 455 66H20Q2 66 0 50Z" fill="var(--maroon-soft)"/>
  </svg>
  <div class="abs pattern" role="img" aria-label="Faint circular key-pattern ornament in the lower right corner"></div>
  <div class="abs mark-frame"><span class="brand-word">BRIGHTFOLD</span></div>
  <div class="abs gold-rule"></div>
</section>

</body>
</html>
```